Business Card Design Project - bel soravin group

dear Sirs

we need business card design for our group ( BEL Soravin Group ) , i have got the Logo design of our group from pixel harbor in previous , so all need details relating to our group i think available with you, as well as the the chosen logo design

we hope to provide us with business card logo that to be appropaite and satisfactory to us .

thanks

note : logo design of our group is attached .
Updates

Reason: please extend the deadline of my project for additional 15 days because i didn't received appropriate design for our gruop yet . kindly beaware that i have received 77 design till now , supossed to send me 200-250 design at least . thanks

Target Market(s)

contents
-

name : Korvan EL Mistrani

position : Operation Manager

Industry/Entity Type

Business

Requirements
Must have

• person name

group logo
Nice to have
• logo color matching with back background

```html
<!DOCTYPE html>
<html lang="en">
<head>
<meta charset="utf-8">
<title>BEL Soravin Group – Business Card</title>
<link href="https://fonts.googleapis.com/css2?family=Arimo:wght@400;700&display=swap" rel="stylesheet">
<style>
  :root {
    --page-bg: #ffffff;
    --card-top: #dfe5f6;
    --card-mid: #8fa4e6;
    --card-bottom: #0a32cc;
    --brand-blue: #1a3fc6;
    --label-gold: #f2d45c;
    --accent-light: #f4e68e;
    --accent-deep: #c99b1f;
  }
  * { margin: 0; padding: 0; box-sizing: border-box; }
  html, body {
    width: 1200px; height: 364px; overflow: hidden;
    background: var(--page-bg);
    font-family: "Arimo", Arial, sans-serif;
  }
  .canvas { position: relative; width: 1200px; height: 364px; }
  .card {
    position: absolute; top: 0; width: 562px; height: 364px;
    border-radius: 24px; overflow: hidden;
    background: linear-gradient(180deg, var(--card-top) 0%, var(--card-mid) 50%, var(--card-bottom) 100%);
  }
  .card--front { left: 0; }
  .card--back { left: 638px; }

  .corner-accent {
    position: absolute; bottom: 0; width: 168px; height: 122px;
    background: linear-gradient(180deg, var(--accent-light) 0%, var(--accent-deep) 100%);
    opacity: 0.85;
  }
  .card--front .corner-accent { left: 0; border-top-right-radius: 100% 30%; }
  .card--back .corner-accent { right: 0; border-top-left-radius: 100% 30%; }

  .brand {
    position: absolute; display: flex; align-items: center;
    color: var(--brand-blue); font-weight: 700; white-space: nowrap;
  }
  .brand__mark { background: var(--brand-blue); flex: none; }
  .card--front .brand { left: 50%; top: 146px; transform: translateX(-50%); font-size: 44px; gap: 16px; }
  .card--front .brand__mark { width: 34px; height: 34px; }
  .card--back .brand { left: 38px; top: 44px; font-size: 24px; gap: 10px; }
  .card--back .brand__mark { width: 18px; height: 18px; }

  .person {
    position: absolute; left: 0; right: 0; top: 144px;
    text-align: center; color: var(--brand-blue);
  }
  .person__name { font-size: 21px; font-weight: 700; }
  .person__role { font-size: 14px; margin-top: 2px; }

  .contacts {
    position: absolute; top: 276px; left: 23px;
    display: grid; grid-template-columns: 185px 160px; row-gap: 2px;
    color: var(--label-gold); font-size: 14px; font-weight: 700; line-height: 17px;
  }
</style>
</head>
<body>
<div class="canvas">
  <section class="card card--front">
    <div class="brand"><span class="brand__mark"></span>BEL Soravin Group</div>
    <div class="corner-accent" role="img" aria-label="Gold swoosh ornament in the lower left corner"></div>
  </section>

  <section class="card card--back">
    <div class="brand"><span class="brand__mark"></span>BEL Soravin Group</div>
    <div class="person">
      <div class="person__name">Korvan EL Mistrani</div>
      <div class="person__role">Operation Manager</div>
    </div>
    <div class="contacts">
      <span>tel :</span><span>email address :</span>
      <span>fax :</span><span>web site :</span>
      <span>mobile :</span><span>PO . Box:</span>
    </div>
    <div class="corner-accent" role="img" aria-label="Gold swoosh ornament in the lower right corner"></div>
  </section>
</div>
</body>
</html>
```